Web Button design and production

I need remote control like buttons (or your own design of buttons if I like it)
3x4 text buttons (normal, pressed, disabled)
3x1 empty button (normal, pressed, disabled)
3x6 buttons with glyph (normal, pressed, disabled)
3x288 with 24h time "00:00", "00:05", "00:10" (normal, pressed, disabled)
4 LED (red, green, orange, black)
I will upload the background image as soon as possible (black plastic)
See attached images
Q: Do the buttons have to be gray/black?
A: It should look like a high end remote control. It could be brushed aluminum as well, or something you come up with. But I guess black or dark grey would be best. The background will be picsharbor 40561739, but it's not available yet.
Q: Do I have to provide all buttons for the contest?
A: No! I only need one button (3 states) and a LED to decide. Only the winner will do the whole job.
Q: Is the Designer who wins the contest expected to complete all the extra buttons?
A: Yes, please.
Plastic

```html
<!DOCTYPE html>
<html lang="en">
<head>
<meta charset="utf-8">
<title>Remote Control Buttons – Plastic</title>
<link rel="stylesheet" href="https://fonts.googleapis.com/css2?family=Lobster&display=swap">
<style>
  :root {
    --bg-center: #333333;
    --bg-edge: #242424;
    --label: #f4f4f4;
    --btn-top: #323232;
    --btn-bottom: #2a2a2a;
    --btn-border: #1b1b1b;
    --btn-highlight: rgba(255,255,255,0.07);
    --btn-pressed: #1d1d1d;
    --icon-normal: #e4e4e4;
    --icon-disabled: #1a1a1a;
    --ring-light: #f2f2f2;
    --ring-dark: #9a9a9a;
    --led-red: #e0161b;
    --led-red-hi: #ff6a6a;
    --led-green: #36b21b;
    --led-green-hi: #8ff06a;
    --led-orange: #f59a00;
    --led-orange-hi: #ffd04a;
    --led-black: #1c1c1c;
    --led-black-hi: #5a5a5a;
  }
  * { margin: 0; padding: 0; box-sizing: border-box; }
  html, body { width: 1200px; height: 1200px; overflow: hidden; }
  body {
    position: relative;
    background: radial-gradient(ellipse at 50% 40%, var(--bg-center) 0%, var(--bg-edge) 80%);
    font-family: "Lobster", cursive;
  }
  .led {
    position: absolute;
    top: 302px;
    width: 92px; height: 92px;
    border-radius: 50%;
    background: linear-gradient(180deg, var(--ring-light) 0%, var(--ring-dark) 100%);
    box-shadow: 0 3px 6px rgba(0,0,0,0.6);
  }
  .led::after {
    content: "";
    position: absolute;
    inset: 12px;
    border-radius: 50%;
    box-shadow: inset 0 2px 4px rgba(0,0,0,0.5);
  }
  .led--red { left: 374px; }
  .led--red::after { background: radial-gradient(circle at 50% 30%, var(--led-red-hi) 0%, var(--led-red) 55%, #9e0a0e 100%); }
  .led--green { left: 494px; }
  .led--green::after { background: radial-gradient(circle at 50% 30%, var(--led-green-hi) 0%, var(--led-green) 55%, #1f7a0e 100%); }
  .led--orange { left: 614px; }
  .led--orange::after { background: radial-gradient(circle at 50% 30%, var(--led-orange-hi) 0%, var(--led-orange) 55%, #b86a00 100%); }
  .led--black { left: 734px; }
  .led--black::after { background: radial-gradient(circle at 50% 30%, var(--led-black-hi) 0%, var(--led-black) 55%, #080808 100%); }

  .state-label {
    position: absolute;
    top: 482px;
    width: 240px;
    text-align: center;
    color: var(--label);
    font-size: 36px;
    text-shadow: 0 2px 3px rgba(0,0,0,0.6);
  }
  .state-label--normal { left: 240px; }
  .state-label--pressed { left: 480px; }
  .state-label--disabled { left: 720px; }

  .remote-button {
    position: absolute;
    top: 576px;
    width: 192px; height: 120px;
    border-radius: 8px;
    border: 2px solid var(--btn-border);
    display: flex; align-items: center; justify-content: center;
  }
  .remote-button svg { width: 58px; height: 42px; }
  .remote-button--normal {
    left: 264px;
    background: linear-gradient(180deg, var(--btn-top), var(--btn-bottom));
    box-shadow: inset 0 2px 0 var(--btn-highlight), 0 3px 6px rgba(0,0,0,0.45);
    color: var(--icon-normal);
  }
  .remote-button--pressed {
    left: 504px;
    background: var(--btn-pressed);
    box-shadow: inset 0 4px 10px rgba(0,0,0,0.7), 0 1px 0 rgba(255,255,255,0.05);
    color: var(--icon-normal);
  }
  .remote-button--disabled {
    left: 744px;
    background: linear-gradient(180deg, var(--btn-top), var(--btn-bottom));
    box-shadow: inset 0 2px 0 var(--btn-highlight), 0 3px 6px rgba(0,0,0,0.45);
    color: var(--icon-disabled);
  }
</style>
</head>
<body>
  <div class="led led--red" aria-label="Red LED"></div>
  <div class="led led--green" aria-label="Green LED"></div>
  <div class="led led--orange" aria-label="Orange LED"></div>
  <div class="led led--black" aria-label="Black LED"></div>

  <div class="state-label state-label--normal">Normal</div>
  <div class="state-label state-label--pressed">Pressed</div>
  <div class="state-label state-label--disabled">Disabled</div>

  <div class="remote-button remote-button--normal" aria-label="Fast forward, normal">
    <svg viewBox="0 0 58 42"><path fill="currentColor" d="M2 2 L28 21 L2 40 Z M28 2 L56 21 L28 40 Z" opacity="0.95"/></svg>
  </div>
  <div class="remote-button remote-button--pressed" aria-label="Fast forward, pressed">
    <svg viewBox="0 0 58 42"><path fill="currentColor" d="M2 2 L28 21 L2 40 Z M28 2 L56 21 L28 40 Z" opacity="0.95"/></svg>
  </div>
  <div class="remote-button remote-button--disabled" aria-label="Fast forward, disabled">
    <svg viewBox="0 0 58 42"><path fill="currentColor" d="M2 2 L28 21 L2 40 Z M28 2 L56 21 L28 40 Z"/></svg>
  </div>
</body>
</html>
```